Core Values Banner For Hearthwell Partners Inc

We want to take the core values for our small growing chimney service company and post them for our entire team to see on a daily basis. We want to be remind everyone how important this is too us all. IntegrityWe try to be honest and accountable in all aspects of our business, as well as in our personal interactions. We do what we say we will do, when we say we will do it, and how we say we will do it.Kaizen“Change for the best”We strive to constantly grow and improve, both personally and professionally. We own up to our mistakes and strive to resolve and learn from them. We actively seek feedback from our clients and each other. We believe the most innovative ideas come when we intentionally look for them.FamilyWe are a family-owned business, and we consider everyone who works here and every one we serve to be part of the family. Being honest and genuine with each other and our customers is what sets us apart. We put ourselves in our customer’s shoes and make recommendations as if it were our chimney, our home and our family.

Font styles to use
Serif
Sans Serif

Colors
ec1f27

Requirements
Must have
• This banner will be approximately 2.5' in height and 6 to 6.5' in width.
• I would like all 3 core values and there definitions listed on the banner
• check out the feel of our marketing on our website www.hearthwellpartnersvt.example

```html
<!DOCTYPE html>
<html lang="en">
<head>
<meta charset="utf-8">
<title>Hearthwell Partners Inc – Core Values Banner</title>
<link href="https://fonts.googleapis.com/css2?family=Arimo&family=PT+Sans:wght@700&family=Roboto:ital,wght@1,900&display=swap" rel="stylesheet">
<style>
  :root {
    --brand-red: #e12a35;
    --ink: #111111;
    --banner-paper: #efefef;
    --stage: #6f6f6f;
    --name-grey: #555555;
  }
  * { margin: 0; padding: 0; box-sizing: border-box; }
  html, body { width: 1200px; height: 900px; overflow: hidden; }
  body { background: var(--stage); position: relative; }

  .banner {
    position: absolute; left: 429px; top: 31px;
    width: 342px; height: 838px;
    background: var(--banner-paper);
    overflow: hidden;
  }
  .banner__top-rule { position: absolute; left: 4px; right: 4px; top: 0; height: 11px; background: var(--brand-red); }
  .brand {
    position: absolute; left: 12px; right: 12px; top: 30px; height: 54px;
    display: flex; align-items: center; justify-content: center;
  }
  .brand__name {
    font-family: "PT Sans", Arial, sans-serif; font-weight: 700;
    font-size: 22px; line-height: 1; color: var(--name-grey); letter-spacing: 0.3px;
    white-space: nowrap;
  }
  .banner__header-rule { position: absolute; left: 5px; right: 5px; top: 105px; height: 12px; background: var(--brand-red); }

  .headline { position: absolute; left: 0; right: 0; text-align: center; font-family: "Roboto", Arial, sans-serif; font-style: italic; font-weight: 900; }
  .headline--core { top: 116px; font-size: 84px; line-height: 86px; color: var(--ink); letter-spacing: 1px; }
  .headline__underline { position: absolute; left: 50px; width: 241px; top: 195px; height: 4px; background: var(--ink); }
  .headline--values { top: 194px; font-size: 72px; line-height: 80px; color: var(--brand-red); letter-spacing: 1px; }

  .chevron { position: absolute; left: 5px; top: 264px; width: 332px; height: 24px; }

  .value { position: absolute; left: 12px; right: 12px; text-align: center; }
  .value__title {
    font-family: "PT Sans", Arial, sans-serif; font-weight: 700;
    color: var(--brand-red); font-size: 26px; line-height: 32px;
  }
  .value__title--large { font-size: 33px; line-height: 38px; }
  .value__body {
    font-family: "Arimo", Arial, sans-serif; color: var(--ink);
    font-size: 14px; line-height: 14.4px; white-space: nowrap;
  }
  .value--integrity { top: 292px; }
  .value--integrity .value__body { margin-top: 10px; line-height: 15.5px; }
  .value--kaizen { top: 435px; }
  .value--family { top: 632px; }
  .value--family .value__body { margin-top: 8px; }

  .banner__foot { position: absolute; left: 0; bottom: 0; width: 342px; height: 22px; }
</style>
</head>
<body>
  <main class="banner">
    <div class="banner__top-rule"></div>

    <header class="brand">
      <span class="brand__name">HEARTHWELL PARTNERS INC</span>
    </header>

    <div class="banner__header-rule"></div>

    <h1>
      <span class="headline headline--core">CORE</span>
      <span class="headline__underline"></span>
      <span class="headline headline--values">VALUES</span>
    </h1>

    <svg class="chevron" viewBox="0 0 332 24" preserveAspectRatio="none" aria-hidden="true">
      <polygon points="0,0 332,0 332,4 166,24 0,4" fill="var(--brand-red)"/>
    </svg>

    <section class="value value--integrity">
      <h2 class="value__title value__title--large">INTEGRITY</h2>
      <p class="value__body">We try to be honest and accountable in all<br>aspects of our business, as well as in our<br>personal interactions. We do what we say<br>we will do, when we say we will do it, and<br>how we say we will do it.</p>
    </section>

    <section class="value value--kaizen">
      <h2 class="value__title">KAIZEN<br>"CHANGE FOR THE BEST"</h2>
      <p class="value__body">We strive to constantly grow and improve,<br>both personally and professionally. We<br>own up to our mistakes and strive to<br>resolve and learn from them. We actively<br>seek feedback from our clients and each<br>other. We believe the most innovative<br>ideas come when we intentionally look for<br>them.</p>
    </section>

    <section class="value value--family">
      <h2 class="value__title">FAMILY</h2>
      <p class="value__body">We are a family-owned business, and we<br>consider everyone who works here and<br>every one we serve to be part of the family.<br>Being honest and genuine with each other<br>and our customers is what sets us apart.<br>We put ourselves in our customer’s shoes<br>and make recommendations as if it were<br>our chimney, our home and our family.</p>
    </section>

    <svg class="banner__foot" viewBox="0 0 342 22" preserveAspectRatio="none" aria-hidden="true">
      <polygon points="0,22 175,0 342,22" fill="var(--brand-red)"/>
    </svg>
  </main>
</body>
</html>
```